Fenmarrow brand new master design

Company Background:
The company Fenmarrow was founded in March 2019 and deals with the IT of the smallest companies. Unlike the PC specialist, no server is needed. Our motto is "just work". This motto aims to make it easy for the user to work without having to deal with the problems of PCs or a main computer.

This project:
We would like to create a Powerpoint Master wich makes us able to create future presentations. We'll need a design to ge it done. We are looking for a design aligned with our website and logo.

Target Market(s)

In a more complicated IT infrastructure it is even harder for small companies to maintain it. Even plumbers, electricians should be able to get a secure and reliable IT infrastructure. We are targeting companies between 1 and 15 IT users. Our customers do not have any ERP software that's just so simple. There is no need to have things like a server onsite anymore. We are providing the service from a safe and secure location within Germany.

Industry/Entity Type

It Company

Other font styles liked:
• Raleway

Requirements
Must have
• What we need to be in the master:
- Title Page (first slide)
- Table of content page
- Subtopic title page (Title with underline)
- Content-PAge with bullet points
- Content split bullet-points and image

We are using Raleway Google font.
Logos attached. Our website: www.fenmarrow.de
Must be aligned to our website and logo.
Nice to have
• selected Stock image gallery

```html
<!DOCTYPE html>
<html lang="en">
<head>
<meta charset="utf-8">
<title>Fenmarrow Presentation Guideline</title>
<link href="https://fonts.googleapis.com/css2?family=Raleway:wght@400;500;600;700;800&display=swap" rel="stylesheet">
<style>
:root{
  --blue:#0a6cb8;
  --navy:#0b4a80;
  --mid:#2a86d0;
  --pale:#dbe8f4;
  --ink:#1b1b1b;
  --grey:#8a8f96;
  --white:#ffffff;
}
*{margin:0;padding:0;box-sizing:border-box}
html,body{width:1200px;height:675px;overflow:hidden;background:#fff}
body{font-family:'Raleway',sans-serif;color:var(--ink);position:relative}
.slide{position:absolute;background:var(--white);overflow:hidden;box-shadow:0 2px 8px rgba(0,0,0,.12)}
.slide.small{width:259px;height:146px}
.abs{position:absolute}
.slide-title{position:absolute;left:13px;top:14px;font-size:9px;font-weight:700;color:var(--ink);white-space:nowrap}
.slide-title span{color:var(--blue)}
.slide-title.underlined::after{content:"";position:absolute;left:0;top:13px;width:18px;height:1.5px;background:var(--blue)}
.brand{position:absolute;left:13px;bottom:5px;font-size:5px;font-weight:800;letter-spacing:.5px;color:var(--blue)}
.brand.light{color:var(--white)}
.page-no{position:absolute;right:13px;bottom:6px;font-size:2.6px;color:var(--grey)}
.page-no.light{color:#cfe0f0}
.tiny{font-size:3.6px;line-height:1.3}
.micro{font-size:3px;line-height:1.3}
.white{color:var(--white)}
.box-blue{background:var(--blue);color:var(--white)}
.box-navy{background:var(--navy);color:var(--white)}

/* title slide */
.title-slide{left:58px;top:34px;width:536px;height:301px}
.title-slide .brand{left:27px;top:26px;bottom:auto;font-size:11px;letter-spacing:1px}
.title-name{left:27px;top:149px;font-size:25px;font-weight:800;color:var(--blue)}
.title-sub{left:27px;top:180px;font-size:22px;font-weight:800;color:var(--ink)}
.title-date{left:27px;top:211px;font-size:11px;font-weight:500}

/* steps */
.step{position:absolute;top:46px;width:55px;height:77px;padding:5px 4px}
.step h4{font-size:6px;font-weight:700;line-height:1.1;margin-top:17px;margin-bottom:3px}
.step .num{position:absolute;right:3px;top:1px;font-size:9px;font-weight:800;color:rgba(0,0,0,.35)}
.step .ico{position:absolute;left:5px;top:8px;width:8px;height:10px;border:1px solid #fff;border-radius:1px}
.arrow{position:absolute;top:78px;width:7px;height:7px;border-radius:50%;background:#fff;z-index:2}
.arrow::after{content:"";position:absolute;left:2.2px;top:1.8px;width:2px;height:2px;border-right:1px solid var(--navy);border-top:1px solid var(--navy);transform:rotate(45deg)}

/* service cards */
.band{position:absolute;left:0;right:0;top:72px;height:56px;background:var(--pale)}
.card{position:absolute;top:58px;width:61px;height:72px;padding:5px}
.card h4{font-size:4.8px;font-weight:800;line-height:1.1;margin-bottom:4px}
.card .feat{font-size:3.4px;font-weight:700;margin-bottom:1px}
.card ul{list-style:none}
.card li{font-size:3px;line-height:1.3}
.card li::before{content:"✓ "}
.card .cta{position:absolute;left:5px;bottom:0;width:45px;height:7px;background:var(--pale);color:var(--blue);font-size:3px;font-weight:700;padding:2px 3px}

/* quotes */
.quote{position:absolute;width:97px;height:39px;padding:4px 6px}
.quote .mark{font-size:6px;font-weight:800;line-height:.8}
.quote .who{font-size:3.4px;font-weight:700;margin-top:2px}
.quote::after{content:"";position:absolute;right:14px;bottom:-4px;border-left:4px solid transparent;border-right:4px solid transparent;border-top:4px solid currentColor}
.quote.box-blue::after{border-top-color:var(--blue)}
.quote.box-navy::after{border-top-color:var(--navy)}

/* benefits */
.benefit{position:absolute;width:75px;height:29px;display:flex;align-items:center;padding-left:10px;gap:8px}
.benefit i{display:block;width:9px;height:9px;border:1.2px solid #fff;border-radius:50%;flex:none}
.benefit b{font-size:6px;font-weight:700;line-height:1.05;color:#fff}

/* section slide */
.section-slide{background:var(--blue)}
.section-title{left:13px;top:81px;font-size:10px;font-weight:700;color:#fff}
.section-body{left:13px;top:96px;width:150px;color:#fff}

/* toc */
.toc-panel{position:absolute;left:105px;top:0;width:154px;height:134px;background:var(--blue);border-bottom-left-radius:14px}
.toc-list{position:absolute;left:113px;top:17px;width:134px;list-style:none}
.toc-list li{display:flex;justify-content:space-between;color:#fff;font-size:6.4px;height:13.4px}
.toc-list li span:first-child::before{content:"• "}

/* chart side boxes */
.chart-box{position:absolute;left:177px;width:69px;height:39px;padding:5px 6px}
.chart-box h4{font-size:6px;font-weight:700;margin-bottom:2px}
.chart-box p{font-size:4.2px;line-height:1.2}

/* ring slide */
.ring-label{position:absolute;width:60px}
.ring-label h5{font-size:5px;font-weight:700;color:var(--blue)}
.ring-label p{font-size:3.2px;line-height:1.2;color:#444}
.ring-label.left{text-align:right}

/* bullet slide */
.bullets{position:absolute;left:13px;top:34px;width:232px;font-size:4.9px;line-height:1.25;list-style:none}
.bullets>li{padding-left:5px;position:relative;margin-bottom:2px}
.bullets>li::before{content:"•";position:absolute;left:0}
.bullets ul{list-style:none;margin-top:1px}
.bullets ul li{font-size:4.3px;padding-left:7px;position:relative}
.bullets ul li::before{content:"–";position:absolute;left:1px}

/* problem/solution */
.ps-box{position:absolute;top:64px;width:59px;height:64px;padding:5px 6px}
.ps-box h4{font-size:5.2px;font-weight:700;margin:9px 0 2px}
.ps-box .ico{position:absolute;left:6px;top:5px;width:6px;height:6px;border:1px solid #fff;border-radius:50%}

/* services development */
.map-panel{position:absolute;left:135px;top:0;width:124px;height:146px;background:var(--pale)}
.svc{position:absolute;left:13px;display:flex;align-items:center;gap:5px}
.svc i{width:8px;height:8px;background:var(--navy);color:#fff;font-style:normal;font-size:4px;font-weight:700;display:flex;align-items:center;justify-content:center}
.svc b{font-size:5.2px;font-weight:700;color:var(--navy)}

/* thank you */
.thanks-slide{background:var(--blue)}
</style>
</head>
<body>

<!-- Title slide -->
<section class="slide title-slide">
  <div class="brand">FENMARROW</div>
  <div class="abs title-name">Fenmarrow</div>
  <div class="abs title-sub">Presentation Guideline</div>
  <div class="abs title-date">May 2020</div>
  <svg class="abs" style="left:325px;top:0" width="211" height="301" viewBox="0 0 211 301">
    <path d="M40 0 H211 V270 L70 301 Q10 305 8 250 L0 60 Q0 5 40 0 Z" fill="#b9d3ec"/>
    <path role="img" aria-label="Hands typing on a laptop keyboard, blue-toned photograph" d="M60 0 H211 V258 L90 285 Q38 292 35 240 L25 45 Q25 0 60 0 Z" fill="url(#photoTone)"/>
    <defs><linearGradient id="photoTone" x1="0" y1="0" x2="1" y2="1"><stop offset="0" stop-color="#1f6fb6"/><stop offset=".55" stop-color="#4f8fc8"/><stop offset="1" stop-color="#0d4d86"/></linearGradient></defs>
  </svg>
</section>

<!-- How do I become a customer -->
<section class="slide small" style="left:613px;top:34px">
  <div class="slide-title"><span>How Do I Become a</span> Customer?</div>
  <div class="abs" style="left:13px;top:36px;font-size:4.2px;font-weight:700">The following four steps are required to become a Fenmarrow customer.</div>
  <div class="step box-blue" style="left:13px"><i class="ico"></i><span class="num">1</span><h4>Select<br>service</h4><p class="micro">Fenmarrow offers two different models. Choose one of these models.</p></div>
  <div class="step box-navy" style="left:72px"><i class="ico"></i><span class="num">2</span><h4>Send<br>an inquiry</h4><p class="micro">Fill out our non-binding contract inquiry form. We draw up a contract.</p></div>
  <div class="step box-blue" style="left:131px"><i class="ico"></i><span class="num">3</span><h4>Sign<br>a contract</h4><p class="micro">You can send us the signed contract by post or by email.</p></div>
  <div class="step box-navy" style="left:190px"><i class="ico"></i><span class="num">4</span><h4>Lot<br>work</h4><p class="micro">As soon as the contract is received, you can start working within five working days.</p></div>
  <i class="arrow" style="left:65px"></i><i class="arrow" style="left:124px"></i><i class="arrow" style="left:183px"></i>
  <div class="brand">FENMARROW</div><div class="page-no">Page | 6</div>
</section>

<!-- Select service -->
<section class="slide small" style="left:891px;top:34px">
  <div class="slide-title"><span>Select</span> Service</div>
  <p class="abs micro" style="left:13px;top:35px;width:232px;font-size:3.4px">Choose your service. Fenmarrow provides a complete workstation in the thin client model. All you need is a monitor to start working. Both services can be used encrypted from any location with an existing PC, laptop or tablet.</p>
  <div class="band"></div>
  <div class="card box-blue" style="left:33px"><h4>THIN<br>CLIENT</h4><div class="feat">Features</div><ul><li>Billing per user</li><li>Thin client per user included</li><li>Licensed operating system</li><li>Max. 8 hours reaction time</li></ul><div class="cta">GET STARTED NOW</div></div>
  <div class="card box-navy" style="left:98px"><h4>MOBILE<br>THIN CLIENT</h4><div class="feat">Features</div><ul><li>Billing per user</li><li>Support and management</li><li>Licensed operating system</li><li>Max. 8 hours reaction time</li></ul><div class="cta">GET STARTED NOW</div></div>
  <div class="card box-blue" style="left:164px"><h4>BRING<br>YOUR OWN</h4><div class="feat">Features</div><ul><li>Billing per user</li><li>Use with your own device</li><li>Licensed operating system</li><li>Max. 8 hours reaction time</li></ul><div class="cta">GET STARTED NOW</div></div>
  <div class="brand">FENMARROW</div><div class="page-no">Page | 7</div>
</section>

<!-- Customers say -->
<section class="slide small" style="left:613px;top:190px">
  <div class="slide-title"><span>What Our</span> Customers Say</div>
  <div class="quote box-blue" style="left:29px;top:37px"><div class="mark">“</div><p class="micro">I can work anywhere. Competitors had to file for bankruptcy after a cryptovirus. My data is safe.</p><div class="who">- Property manager</div></div>
  <div class="quote box-navy" style="left:133px;top:37px"><div class="mark">“</div><p class="micro">We have grown in recent years. With Fenmarrow we have found a solution that scales without one-off costs.</p><div class="who">- electrician</div></div>
  <div class="quote box-navy" style="left:29px;top:84px"><div class="mark">“</div><p class="micro">I recently started my company. The monthly payment for the services offers great financial flexibility.</p><div class="who">- Quality consultant</div></div>
  <div class="quote box-blue" style="left:133px;top:84px"><div class="mark">“</div><p class="micro">For us, Fenmarrow solved significant problems with the speed in our software. We are happy now.</p><div class="who">- Retailers</div></div>
  <div class="brand">FENMARROW</div><div class="page-no">Page | 8</div>
</section>

<!-- Benefits -->
<section class="slide small" style="left:891px;top:190px">
  <div class="slide-title"><span>An Overview</span> Of Your Benefits</div>
  <div class="benefit box-blue" style="left:13px;top:34px"><i></i><b>Express Interference Suppression</b></div>
  <div class="benefit box-navy" style="left:92px;top:34px"><i></i><b>Fast<br>Programs</b></div>
  <div class="benefit box-blue" style="left:171px;top:34px"><i></i><b>Professional Protection</b></div>
  <div class="benefit box-navy" style="left:13px;top:67px"><i></i><b>Data<br>Backup</b></div>
  <div class="benefit box-blue" style="left:92px;top:67px"><i></i><b>Sustainable</b></div>
  <div class="benefit box-navy" style="left:171px;top:67px"><i></i><b>Predictable Costs</b></div>
  <div class="benefit box-blue" style="left:13px;top:99px"><i></i><b>Updates</b></div>
  <div class="benefit box-navy" style="left:92px;top:99px"><i></i><b>High<br>Security</b></div>
  <div class="benefit box-blue" style="left:171px;top:99px"><i></i><b>Familiar Software</b></div>
  <div class="brand">FENMARROW</div><div class="page-no">Page | 9</div>
</section>

<!-- Section slide -->
<section class="slide small section-slide" style="left:58px;top:345px">
  <svg class="abs" style="left:170px;top:8px" width="89" height="130" viewBox="0 0 89 130">
    <path d="M25 2 H89 V126 L35 130 Q12 130 10 108 L2 25 Q0 4 25 2 Z" fill="#3d8fd3" opacity=".55"/>
    <path d="M40 12 H89 V112 L52 116 Q32 118 30 98 L22 32 Q20 13 40 12 Z" fill="none" stroke="#8dbbe6" stroke-width="5"/>
  </svg>
  <div class="abs section-title">Section Slide Title</div>
  <p class="abs section-body tiny">Lorem Ipsum is simply dummy text of the printing and typesetting industry. Lorem Ipsum has been the industry's standard dummy text ever since the 1500s.</p>
  <div class="brand light">FENMARROW</div><div class="page-no light">Page | 2</div>
</section>

<!-- Table of content -->
<section class="slide small" style="left:336px;top:345px">
  <div class="slide-title underlined"><span>Table</span> of Content</div>
  <div class="toc-panel"></div>
  <ul class="toc-list">
    <li><span>Introduce</span><span>2</span></li>
    <li><span>About</span><span>4</span></li>
    <li><span>Our Services</span><span>6</span></li>
    <li><span>Performance per Years</span><span>8</span></li>
    <li><span>Organizations</span><span>10</span></li>
    <li><span>Future Plan</span><span>15</span></li>
  </ul>
  <div class="brand">FENMARROW</div><div class="page-no">Page | 3</div>
</section>

<!-- Chart -->
<section class="slide small" style="left:613px;top:345px">
  <div class="slide-title underlined"><span>Chart</span> Example</div>
  <svg class="abs" style="left:13px;top:38px" width="156" height="90" viewBox="0 0 156 90">
    <text x="78" y="6" font-size="4.2" font-weight="700" fill="#0a6cb8" text-anchor="middle" font-family="Raleway, sans-serif">Performance per Years</text>
    <g stroke="#e4e8ee" stroke-width=".4">
      <line x1="8" y1="12" x2="8" y2="78"/><line x1="23" y1="12" x2="23" y2="78"/><line x1="38" y1="12" x2="38" y2="78"/><line x1="53" y1="12" x2="53" y2="78"/><line x1="68" y1="12" x2="68" y2="78"/><line x1="83" y1="12" x2="83" y2="78"/><line x1="98" y1="12" x2="98" y2="78"/><line x1="113" y1="12" x2="113" y2="78"/><line x1="128" y1="12" x2="128" y2="78"/><line x1="143" y1="12" x2="143" y2="78"/>
    </g>
    <line x1="0" y1="78" x2="156" y2="78" stroke="#c6ccd4" stroke-width=".5"/>
    <polyline points="8,53 23,49 38,48 53,45 68,41 83,32 98,28 113,34 128,28 143,24" fill="none" stroke="#0b4a80" stroke-width=".8"/>
    <polyline points="8,60 23,56 38,57 53,54 68,52 83,37 98,31 113,30 128,31 143,31" fill="none" stroke="#0b4a80" stroke-width=".8"/>
    <g fill="#0b4a80">
      <circle cx="8" cy="53" r="1.4"/><circle cx="23" cy="49" r="1.4"/><circle cx="38" cy="48" r="1.4"/><circle cx="53" cy="45" r="1.4"/><circle cx="68" cy="41" r="1.4"/><circle cx="83" cy="32" r="1.4"/><circle cx="98" cy="28" r="1.4"/><circle cx="113" cy="34" r="1.4"/><circle cx="128" cy="28" r="1.4"/><circle cx="143" cy="24" r="1.4"/>
      <circle cx="8" cy="60" r="1.4"/><circle cx="23" cy="56" r="1.4"/><circle cx="38" cy="57" r="1.4"/><circle cx="53" cy="54" r="1.4"/><circle cx="68" cy="52" r="1.4"/><circle cx="83" cy="37" r="1.4"/><circle cx="98" cy="31" r="1.4"/><circle cx="113" cy="30" r="1.4"/><circle cx="128" cy="31" r="1.4"/><circle cx="143" cy="31" r="1.4"/>
    </g>
    <g font-size="2.6" fill="#8a8f96" text-anchor="middle" font-family="Raleway, sans-serif">
      <text x="8" y="83">2010</text><text x="23" y="83">2011</text><text x="38" y="83">2012</text><text x="53" y="83">2013</text><text x="68" y="83">2014</text><text x="83" y="83">2015</text><text x="98" y="83">2016</text><text x="113" y="83">2017</text><text x="128" y="83">2018</text><text x="143" y="83">2019</text>
    </g>
  </svg>
  <div class="chart-box box-blue" style="top:41px"><h4>Select Line A</h4><p>Fenmarrow offers two different models. Choose one of these models.</p></div>
  <div class="chart-box box-navy" style="top:83px"><h4>Select Line B</h4><p>Fenmarrow offers two different models. Choose one of these models.</p></div>
  <div class="brand">FENMARROW</div><div class="page-no">Page | 10</div>
</section>

<!-- Ring slide -->
<section class="slide small" style="left:891px;top:345px">
  <div class="slide-title underlined"><span>Slide</span> Example</div>
  <svg class="abs" style="left:82px;top:32px" width="92" height="92" viewBox="0 0 92 92">
    <circle cx="46" cy="46" r="35" fill="none" stroke="#0a6cb8" stroke-width="18"/>
    <circle cx="46" cy="46" r="35" fill="none" stroke="#0b4a80" stroke-width="18" stroke-dasharray="27.49 27.49" transform="rotate(-90 46 46)"/>
    <g stroke="#fff" stroke-width="1.4">
      <line x1="46" y1="2" x2="46" y2="90"/><line x1="2" y1="46" x2="90" y2="46"/><line x1="15" y1="15" x2="77" y2="77"/><line x1="77" y1="15" x2="15" y2="77"/>
    </g>
    <circle cx="46" cy="46" r="25" fill="#fff"/>
    <circle cx="46" cy="46" r="21" fill="none" stroke="#0a6cb8" stroke-width="1"/>
    <text x="46" y="44" font-size="6.5" font-weight="700" fill="#0a6cb8" text-anchor="middle" font-family="Raleway, sans-serif">Main</text>
    <text x="46" y="51" font-size="6.5" font-weight="700" fill="#0a6cb8" text-anchor="middle" font-family="Raleway, sans-serif">Core</text>
    <text x="46" y="56" font-size="2.6" fill="#555" text-anchor="middle" font-family="Raleway, sans-serif">The quick brown fox jumps</text>
    <g fill="none" stroke="#fff" stroke-width=".8">
      <circle cx="58" cy="14" r="3"/><circle cx="78" cy="34" r="3"/><circle cx="78" cy="58" r="3"/><circle cx="58" cy="78" r="3"/><circle cx="34" cy="78" r="3"/><circle cx="14" cy="58" r="3"/><circle cx="14" cy="34" r="3"/><circle cx="34" cy="14" r="3"/>
    </g>
  </svg>
  <div class="ring-label left" style="left:16px;top:40px"><h5>Title Edit</h5><p>The quick brown fox jumps over the lazy dog.</p></div>
  <div class="ring-label left" style="left:16px;top:62px"><h5>Title Edit</h5><p>The quick brown fox jumps over the lazy dog.</p></div>
  <div class="ring-label left" style="left:16px;top:85px"><h5>Title Edit</h5><p>The quick brown fox jumps over the lazy dog.</p></div>
  <div class="ring-label left" style="left:16px;top:107px"><h5>Title Edit</h5><p>The quick brown fox jumps over the lazy dog.</p></div>
  <div class="ring-label" style="left:183px;top:40px"><h5>Title Edit</h5><p>The quick brown fox jumps over the lazy dog.</p></div>
  <div class="ring-label" style="left:183px;top:62px"><h5>Title Edit</h5><p>The quick brown fox jumps over the lazy dog.</p></div>
  <div class="ring-label" style="left:183px;top:85px"><h5>Title Edit</h5><p>The quick brown fox jumps over the lazy dog.</p></div>
  <div class="ring-label" style="left:183px;top:107px"><h5>Title Edit</h5><p>The quick brown fox jumps over the lazy dog.</p></div>
  <div class="brand">FENMARROW</div><div class="page-no">Page | 11</div>
</section>

<!-- Bullet slide -->
<section class="slide small" style="left:58px;top:500px">
  <div class="slide-title underlined"><span>Slide</span> Example</div>
  <ul class="bullets">
    <li>Lorem Ipsum is simply dummy text of the printing and typesetting industry. Lorem Ipsum has been the industry's standard dummy text ever since the 1500s.</li>
    <li>It has survived not only five centuries, but also the leap into electronic typesetting, remaining essentially unchanged. It was popularised in the 1960s.
      <ul>
        <li>There are many variations of passages of Lorem Ipsum available.</li>
        <li>If you are going to use a passage of Lorem Ipsum.</li>
        <li>It uses a dictionary of over 200 Latin words.</li>
      </ul>
    </li>
  </ul>
  <div class="brand">FENMARROW</div><div class="page-no">Page | 4</div>
</section>

<!-- Split slide -->
<section class="slide small" style="left:336px;top:500px">
  <div class="slide-title underlined"><span>Slide</span> Example</div>
  <svg class="abs" style="left:13px;top:32px" width="95" height="108" viewBox="0 0 95 108">
    <path d="M14 0 H80 Q95 0 95 15 V88 Q95 100 82 101 L20 106 Q4 108 3 92 L0 14 Q0 0 14 0 Z" fill="#b9d3ec"/>
    <path role="img" aria-label="Hands typing on a laptop, blue-toned photograph" d="M24 6 H80 Q92 6 92 18 V84 Q92 95 80 96 L30 100 Q16 101 15 88 L11 20 Q11 6 24 6 Z" fill="url(#laptopTone)"/>
    <defs><linearGradient id="laptopTone" x1="0" y1="0" x2="1" y2="1"><stop offset="0" stop-color="#1c4f82"/><stop offset=".5" stop-color="#5f93c4"/><stop offset="1" stop-color="#123d68"/></linearGradient></defs>
  </svg>
  <p class="abs" style="left:116px;top:39px;width:132px;font-size:4.4px;line-height:1.25"><b style="color:var(--blue)">Lorem Ipsum is simply dummy text of the printing and typesetting industry.</b> Lorem Ipsum has been the industry's standard dummy text ever since the 1500s.</p>
  <div class="ps-box box-blue" style="left:116px"><i class="ico"></i><h4>The Problem</h4><p class="micro">In addition to the human factor, the basis of IT problems is often the computer itself. Viruses land there, programs become lame and data is lost.</p></div>
  <div class="ps-box box-navy" style="left:184px"><i class="ico"></i><h4>Our Solution</h4><p class="micro">Fenmarrow offers you a solution that ensures daily backup of your data and the monitoring of your system. Everything runs in our data center.</p></div>
  <div class="brand">FENMARROW</div><div class="page-no">Page | 5</div>
</section>

<!-- Services development -->
<section class="slide small" style="left:613px;top:500px">
  <div class="map-panel"></div>
  <div class="slide-title"><span>Our Services</span> Development</div>
  <p class="abs" style="left:13px;top:39px;width:117px;font-size:4.4px;line-height:1.2"><b style="color:var(--blue)">Lorem Ipsum is simply dummy text of the printing and typesetting industry.</b> Lorem Ipsum has been the industry's standard dummy text ever since the 1500s.</p>
  <div class="svc" style="top:67px"><i>1</i><b>Business Essentials</b></div>
  <div class="svc" style="top:83px"><i>2</i><b>Marketing Essentials</b></div>
  <div class="svc" style="top:98px"><i>3</i><b>Business Leaders</b></div>
  <div class="svc" style="top:114px"><i>4</i><b>Corporate Finance &amp; Accounting</b></div>
  <svg class="abs" style="left:143px;top:15px" width="10" height="10" viewBox="0 0 10 10"><rect width="10" height="10" fill="#0a6cb8"/><path d="M5 2 a2 2 0 0 1 2 2 c0 1.5-2 4-2 4 s-2-2.5-2-4 a2 2 0 0 1 2-2z" fill="#fff"/></svg>
  <div class="abs" style="left:157px;top:15px;font-size:6.5px;font-weight:700;color:var(--blue);line-height:1.05">Services<br>Location</div>
  <p class="abs micro" style="left:157px;top:31px;width:42px;color:#555">A business is defined as an organization engaged in commercial or professional activities.</p>
  <div class="abs" role="img" aria-label="Map of service locations with highlighted regions" style="left:147px;top:62px;width:102px;height:62px;background:linear-gradient(135deg,#a8c8e8,#7fb0de);border-radius:18px 28px 22px 14px"></div>
  <div class="brand">FENMARROW</div><div class="page-no">Page | 12</div>
</section>

<!-- Thank you -->
<section class="slide small thanks-slide" style="left:891px;top:500px">
  <svg class="abs" style="left:196px;top:35px" width="63" height="100" viewBox="0 0 63 100">
    <path d="M20 2 H63 V96 L28 100 Q10 100 9 84 L2 20 Q1 3 20 2 Z" fill="#3d8fd3" opacity=".55"/>
    <path d="M32 12 H63 V84 L38 88 Q24 89 23 75 L17 28 Q16 13 32 12 Z" fill="none" stroke="#8dbbe6" stroke-width="4"/>
  </svg>
  <div class="abs" style="left:13px;top:14px;font-size:9px;font-weight:700;color:#fff">Thank You</div>
  <p class="abs micro white" style="left:13px;top:28px;width:148px">Lorem Ipsum is simply dummy text of the printing and typesetting industry. Lorem Ipsum has been the industry's standard dummy text ever since the 1500s, when an unknown printer took a galley of type and scrambled it to make a type specimen book. It has survived not only five centuries, but also the leap into electronic typesetting, remaining essentially unchanged.</p>
  <p class="abs micro white" style="left:13px;top:51px;width:148px">It was popularised in the 1960s with the release of sheets containing passages, and more recently with desktop publishing software including versions of Lorem Ipsum.</p>
  <div class="brand light">FENMARROW</div><div class="page-no light">Page | 13</div>
</section>

</body>
</html>
```